Bref créative
Stationary Pack
Business Cards, Letterheads, fax etc
Professional
Luc-Henri Dorsay, MEE, MBME, MHIT, MBHA, ID-Ph.D
Senior Executive Consultant
9 Brindle Way, Suite 305
Toronto ON K7R4B9
Canada
luc-henri.dorsay@vextorian.example
www.vextorian.example
We require the following in our pack: Business cards, fax cover sheets, letterheads, envelopes, CD cases & labels, Email signatures,
Business Consulting and Professional Services Portfolio:
- eHealth consulting and research
- Healthcare IT project management
- Biomedical and health informatics
- Hospital and clinical engineering
- Business analysis and management
- Clean energy and technology management
- eLearning and knowledge translation

```html
<!DOCTYPE html>
<html lang="en">
<head>
<meta charset="utf-8">
<title>Vextorian Stationery Pack</title>
<link href="https://fonts.googleapis.com/css2?family=Montserrat:wght@400;600&display=swap" rel="stylesheet">
<style>
:root{
  --stage:#4b5157;
  --paper:#ffffff;
  --ink:#3c4047;
  --muted:#8b9097;
  --brand-blue:#2f7fc1;
  --brand-green:#6cbf3a;
  --envelope-black:#121212;
  --swoosh-blue:rgba(47,127,193,.22);
  --swoosh-green:rgba(108,191,58,.22);
}
*{box-sizing:border-box;margin:0;padding:0}
html,body{width:1200px;height:326px;overflow:hidden;background:var(--stage)}
body{position:relative;font-family:"Montserrat",Arial,sans-serif;color:var(--ink)}
.piece{position:absolute;background:var(--paper);overflow:hidden;box-shadow:0 1px 3px rgba(0,0,0,.35)}
.label{position:absolute;font-size:4px;color:#e4e6e8;text-align:center;letter-spacing:.2px}
.wordmark{display:flex;align-items:center;gap:2px;font-weight:600;color:var(--brand-blue);letter-spacing:.6px;white-space:nowrap}
.wordmark .dot{width:5px;height:5px;border-radius:50%;background:var(--brand-green)}
.wordmark.on-dark{color:#ffffff}
.swoosh{position:absolute;border-radius:50%;background:radial-gradient(ellipse at 40% 60%,var(--swoosh-blue),var(--swoosh-green) 45%,transparent 70%)}
.bar{position:absolute;left:0;right:0;bottom:0;height:4px;display:flex}
.bar span:first-child{flex:3;background:var(--brand-blue)}
.bar span:last-child{flex:1;background:var(--brand-green)}
.tiny{font-size:3px;line-height:4.4px;color:var(--muted)}
.fax-table{position:absolute;left:8px;right:8px;top:40px;border-collapse:collapse;font-size:3.2px}
.fax-table td{border:.5px solid #bfc3c8;height:7px;padding:0 2px}
.fax-table .head td{background:#2c2f33;color:#fff;height:5px}
.checks{position:absolute;left:8px;right:8px;top:82px;display:flex;justify-content:space-between;font-size:3px;color:var(--muted)}
.checks span::before{content:"";display:inline-block;width:3px;height:3px;border:.5px solid var(--muted);margin-right:1px;vertical-align:middle}
</style>
</head>
<body>

<!-- Business cards -->
<div class="label" style="left:12px;top:20px;width:92px">Business Cards</div>
<div class="piece card-front" style="left:12px;top:30px;width:92px;height:52px">
  <div class="wordmark" style="position:absolute;left:6px;top:8px;font-size:6px"><i class="dot"></i>VEXTORIAN</div>
  <div class="tiny" style="position:absolute;left:6px;top:22px;color:var(--ink)">Luc-Henri Dorsay<br>Senior Executive Consultant</div>
  <div class="tiny" style="position:absolute;left:6px;top:33px;font-size:2.4px;line-height:3.2px">luc-henri.dorsay@vextorian.example<br>www.vextorian.example</div>
  <div class="bar"><span></span><span></span></div>
</div>
<div class="piece card-back" style="left:12px;top:96px;width:92px;height:52px">
  <div class="swoosh" role="img" aria-label="Faint brand swoosh backdrop" style="left:20px;top:-10px;width:90px;height:70px"></div>
  <div class="wordmark" style="position:absolute;left:24px;top:22px;font-size:7px"><i class="dot"></i>VEXTORIAN</div>
</div>

<!-- Envelopes -->
<div class="label" style="left:110px;top:20px;width:160px">Envelopes</div>
<div class="piece envelope" style="left:110px;top:34px;width:160px;height:72px">
  <div class="wordmark" style="position:absolute;left:8px;top:8px;font-size:6px"><i class="dot"></i>VEXTORIAN</div>
  <div class="tiny" style="position:absolute;left:8px;top:18px;font-size:2.6px;line-height:3.4px">9 Brindle Way, Suite 305<br>Toronto ON K7R4B9 Canada</div>
  <div class="bar"><span></span><span></span></div>
</div>
<div class="piece envelope-black" style="left:110px;top:125px;width:160px;height:60px;background:var(--envelope-black)">
  <div class="swoosh" role="img" aria-label="Brand swoosh decoration" style="left:10px;top:-8px;width:110px;height:76px"></div>
  <div class="wordmark on-dark" style="position:absolute;left:96px;top:26px;font-size:6px"><i class="dot"></i>VEXTORIAN</div>
</div>
<div class="piece envelope-blue" style="left:110px;top:194px;width:160px;height:60px;background:var(--brand-blue)">
  <div class="swoosh" role="img" aria-label="Brand swoosh decoration" style="left:10px;top:-8px;width:110px;height:76px;background:radial-gradient(ellipse,rgba(255,255,255,.3),transparent 70%)"></div>
  <div class="wordmark on-dark" style="position:absolute;left:96px;top:26px;font-size:6px"><i class="dot"></i>VEXTORIAN</div>
</div>
<div class="piece envelope-green" style="left:110px;top:263px;width:160px;height:60px;background:var(--brand-green)">
  <div class="swoosh" role="img" aria-label="Brand swoosh decoration" style="left:10px;top:-8px;width:110px;height:76px;background:radial-gradient(ellipse,rgba(255,255,255,.3),transparent 70%)"></div>
  <div class="wordmark on-dark" style="position:absolute;left:96px;top:26px;font-size:6px"><i class="dot" style="background:#fff"></i>VEXTORIAN</div>
</div>

<!-- Letterhead -->
<div class="label" style="left:286px;top:20px;width:132px">Letterhead</div>
<div class="piece letterhead" style="left:286px;top:28px;width:132px;height:190px">
  <div class="wordmark" style="position:absolute;left:8px;top:9px;font-size:6px"><i class="dot"></i>VEXTORIAN</div>
  <div class="tiny" style="position:absolute;left:64px;top:8px;font-size:2.4px;line-height:3.2px">9 Brindle Way, Suite 305<br>Toronto ON K7R4B9 Canada<br>www.vextorian.example</div>
  <div class="swoosh" role="img" aria-label="Faint brand swoosh watermark" style="left:20px;top:100px;width:110px;height:90px"></div>
  <div class="bar"><span></span><span></span></div>
</div>

<div class="label" style="left:424px;top:20px;width:132px">Second Page</div>
<div class="piece letterhead-second" style="left:424px;top:28px;width:132px;height:190px">
  <div class="wordmark" style="position:absolute;left:8px;top:9px;font-size:6px"><i class="dot"></i>VEXTORIAN</div>
  <div class="swoosh" role="img" aria-label="Faint brand swoosh watermark" style="left:20px;top:100px;width:110px;height:90px"></div>
  <div class="bar"><span></span><span></span></div>
</div>

<!-- Fax cover sheets -->
<div class="label" style="left:562px;top:20px;width:132px">Fax Cover Sheet</div>
<div class="piece fax-cover" style="left:562px;top:28px;width:132px;height:190px">
  <div class="wordmark" style="position:absolute;left:8px;top:9px;font-size:6px"><i class="dot"></i>VEXTORIAN</div>
  <div class="tiny" style="position:absolute;left:64px;top:8px;font-size:2.4px;line-height:3.2px">9 Brindle Way, Suite 305<br>Toronto ON K7R4B9 Canada<br>www.vextorian.example</div>
  <table class="fax-table">
    <tr class="head"><td colspan="4">FAX</td></tr>
    <tr><td>To</td><td></td><td>From</td><td></td></tr>
    <tr><td>Fax</td><td></td><td>Phone</td><td></td></tr>
    <tr><td>Date</td><td></td><td>Pages</td><td></td></tr>
    <tr><td>Re</td><td></td><td>CC</td><td></td></tr>
  </table>
  <div class="checks"><span>Urgent</span><span>Review</span><span>Reply</span><span>Recycle</span></div>
  <div class="swoosh" role="img" aria-label="Faint brand swoosh watermark" style="left:20px;top:100px;width:110px;height:90px"></div>
  <div class="bar"><span></span><span></span></div>
</div>

<div class="label" style="left:700px;top:20px;width:132px">Fax Cover Blank</div>
<div class="piece fax-cover-blank" style="left:700px;top:28px;width:132px;height:190px">
  <div class="wordmark" style="position:absolute;left:8px;top:9px;font-size:6px"><i class="dot"></i>VEXTORIAN</div>
  <div class="tiny" style="position:absolute;left:64px;top:8px;font-size:2.4px;line-height:3.2px">9 Brindle Way, Suite 305<br>Toronto ON K7R4B9 Canada<br>www.vextorian.example</div>
  <table class="fax-table">
    <tr class="head"><td colspan="4">FAX</td></tr>
    <tr><td>To</td><td></td><td>From</td><td></td></tr>
    <tr><td>Fax</td><td></td><td>Phone</td><td></td></tr>
    <tr><td>Date</td><td></td><td>Pages</td><td></td></tr>
    <tr><td>Re</td><td></td><td>CC</td><td></td></tr>
  </table>
  <div class="checks"><span>Urgent</span><span>Review</span><span>Reply</span><span>Recycle</span></div>
  <div class="swoosh" role="img" aria-label="Faint brand swoosh watermark" style="left:20px;top:100px;width:110px;height:90px"></div>
  <div class="bar"><span></span><span></span></div>
</div>

<!-- Compliment slip -->
<div class="label" style="left:862px;top:20px;width:64px">Compliment Slip</div>
<div class="piece slip" style="left:862px;top:28px;width:64px;height:40px">
  <div class="wordmark" style="position:absolute;left:5px;top:6px;font-size:4.5px"><i class="dot" style="width:4px;height:4px"></i>VEXTORIAN</div>
  <div class="tiny" style="position:absolute;left:5px;top:16px;font-size:2.2px;line-height:3px">Luc-Henri Dorsay<br>Senior Executive Consultant<br>www.vextorian.example</div>
  <div class="bar" style="height:2px"><span></span><span></span></div>
</div>

<!-- Email signature -->
<div class="label" style="left:982px;top:20px;width:140px">Email Signature</div>
<div class="piece email-signature" style="left:982px;top:28px;width:140px;height:220px">
  <div class="tiny" style="position:absolute;left:10px;top:14px;font-size:3.2px;line-height:5px;color:var(--ink)">
    <strong>Luc-Henri Dorsay</strong><br>Senior Executive Consultant<br>luc-henri.dorsay@vextorian.example<br>www.vextorian.example
  </div>
  <div class="tiny" style="position:absolute;left:10px;top:44px;font-size:2.8px;line-height:5px">
    eHealth consulting and research<br>Healthcare IT project management<br>Biomedical and health informatics<br>Hospital and clinical engineering<br>Business analysis and management<br>Clean energy and technology management<br>eLearning and knowledge translation
  </div>
  <div class="wordmark" style="position:absolute;left:10px;top:88px;font-size:6px"><i class="dot"></i>VEXTORIAN</div>
</div>

</body>
</html>
```